a Label for a candle jar and its gift box

I would like a label that is modern minimalist for candles jars. These jars are colored as white, amber and black. I am thinking maybe foiling gold/silver background with logo only and maybe company name in different color that suits the foiling background color/s. I would like a high quality luxurious design that shows the preciousness of this candle. I am open to any ideas you might have for the design but so far I have used a logo only on the jar which I really like BUT I still feel that it is not enough branding for people when you only show them the logo so I am considering adding the business name. Again, I am open to both ideas (with logo only or logo with business name (Velvet Lantern).

IMPORTANT: YOU MAY IGNORE MY DESIGN COMPLETELY AND DO YOUR OWN ONE AS LONG AS YOU KERP THE LOGO DESIGN. YOU MAY ALSO ADJUST THE LOGO A BIT TO SUIT YOUR DESIGN. - sorry im using capital letters to show importance but im not yelling :)
Updates

UPDATE: To clarify, I have uploaded a video called Corvale in the box to show what the current product look like. It is a corvale jar with a logo only and the jar box has a window that shows the jar with the logo on it and the back of that jar box has a bigger version of the label that has more details (i.e. Fragrance name and website link). So to make it clear, I would like to have two versions of the lables: 1. on the jar with minimal info (logo only or logo with the business name) 2. Bigger version of the label with more info to put on the back of the jar box - as described above. The dimensions of the jars are as per this link https://www.plintova.com.au/corvale-medium-base-and-flat-lid-amber-packed-with-lid-on/ The dimensions of the jar box as per this link https://www.plintova.com.au/corvale-medium-flat-lid-candle-box-with-window-beige/ Looking forward to some artistic productions :)

Update #2: Tues 25 Dec 18 1. I have uploaded the photo which has the logo with the name 'Velvet Lantern' below it just for a reference. However, I would like the designer to modify the current font and NOT to use it as the word 'of in the phrase 'Velvet Lantern' does not come out clear enough after printing. 2. I would like the designer NOT to create a design that will require a clear sticker/label for printing. 3. I have attached the photos of my current designs on the jars or the jar box just as a reference but please do NOT just use the same fonts and only change background. I am hoping to see something different and more professional than my own design :) Thank you very much!

Font styles to use
Decorative
Script

Requirements
Must have
• I would like them to fit on the three colors of the jars below - white, amber and black. Below is a link to how the jar looks like https://www.plintova.com.au/candle-making-supplies/candle-jars/corvale-candle-jars/?glassware_colour=415,443,417&glassware_size=268
Nice to have
• I would like to have a modern design which is suitable for both feminine and musculine.
Should not have
• shouldnt have so much writing on it!

```html
<!DOCTYPE html>
<html lang="en">
<head>
<meta charset="utf-8">
<title>Velvet Lantern – Turkish Rose Label</title>
<link rel="stylesheet" href="https://fonts.googleapis.com/css2?family=Cinzel:wght@400&family=Playfair+Display:wght@400&display=swap">
<style>
  :root {
    --page: #ffffff;
    --rim: #bdbdbf;
    --gold: #fbbd14;
    --gold-light: #fdd35a;
    --gold-deep: #eaa50a;
    --ink: #2b2b2b;
    --brand-ink: #111111;
    --petal-soft: #fbeef1;
    --petal-mid: #f1c3cd;
    --petal-deep: #ea9aac;
    --serif: "Playfair Display", Georgia, serif;
    --display: "Cinzel", "Playfair Display", Georgia, serif;
  }
  * { margin: 0; padding: 0; box-sizing: border-box; }
  html, body {
    width: 1180px; height: 1200px; overflow: hidden;
    background: var(--page);
  }
  .label {
    position: relative;
    width: 1180px; height: 1200px;
    font-family: var(--serif);
    color: var(--ink);
  }
  .label-art { position: absolute; inset: 0; }
  .brand-name,
  .product-line,
  .tagline,
  .scent-name {
    position: absolute;
    left: 0; width: 1180px;
    text-align: center;
    line-height: 1;
    white-space: nowrap;
    font-weight: 400;
  }
  .brand-name {
    top: 458px;
    font-family: var(--display);
    font-size: 66px;
    letter-spacing: 0.03em;
    text-transform: uppercase;
    color: var(--brand-ink);
  }
  .product-line {
    top: 604px;
    font-size: 60px;
    letter-spacing: -0.01em;
  }
  .tagline {
    top: 738px;
    font-size: 40px;
  }
  .scent-name {
    top: 866px;
    font-size: 68px;
    letter-spacing: -0.01em;
  }
</style>
</head>
<body>
<main class="label">
  <svg class="label-art" width="1180" height="1200" viewBox="0 0 1180 1200">
    <defs>
      <linearGradient id="gold-foil" x1="0" y1="0" x2="1" y2="1">
        <stop offset="0%" stop-color="var(--gold-light)"/>
        <stop offset="45%" stop-color="var(--gold)"/>
        <stop offset="100%" stop-color="var(--gold-deep)"/>
      </linearGradient>
      <linearGradient id="petal-wash" x1="0" y1="0" x2="1" y2="1">
        <stop offset="0%" stop-color="var(--petal-mid)"/>
        <stop offset="35%" stop-color="var(--petal-soft)"/>
        <stop offset="60%" stop-color="var(--petal-mid)"/>
        <stop offset="85%" stop-color="var(--petal-soft)"/>
        <stop offset="100%" stop-color="var(--petal-deep)"/>
      </linearGradient>
      <clipPath id="inner-face">
        <circle cx="590" cy="600" r="433"/>
      </clipPath>
    </defs>

    <!-- outer rim with rose petal backdrop -->
    <circle class="petal-ring" cx="590" cy="600" r="533" fill="url(#petal-wash)"
            role="img" aria-label="Scattered pink rose petals around the label edge"/>
    <circle class="outer-rim" cx="590" cy="600" r="533" fill="none" stroke="var(--rim)" stroke-width="6"/>

    <!-- gold foil frame and white face -->
    <circle class="gold-frame" cx="590" cy="600" r="442" fill="var(--page)" stroke="url(#gold-foil)" stroke-width="18"/>

    <!-- brand mark placeholder -->
    <circle class="brand-dot" cx="590" cy="392" r="26" fill="var(--brand-ink)"/>

    <!-- divider rules -->
    <rect class="rule" x="174" y="580" width="831" height="5" fill="url(#gold-foil)"/>
    <rect class="rule" x="182" y="686" width="815" height="5" fill="url(#gold-foil)"/>

    <!-- scent band -->
    <polygon class="scent-band" clip-path="url(#inner-face)"
             points="265,846 919,846 1080,1100 100,1100" fill="url(#gold-foil)"/>
  </svg>

  <h1 class="brand-name">Velvet Lantern</h1>
  <p class="product-line">Natural Soy Wax Candles</p>
  <p class="tagline">hand poured with passion &amp; care</p>
  <p class="scent-name">Turkish Rose</p>
</main>
</body>
</html>
```